Ridgely Forge business card for handing simple contact information and generating service awareness

Utilizing the attached logo(s), generate a professional, but approachable, card conveying a sense of capability and integrity. Please only use one logo of the four attached; the different colors are all acceptable, but preference will be given to a design integrating a teal/turquoise logo,

I do not know where to put in the contact information or details?

Target Market(s)

Agriculture, Farming, Timber, Forestry, Construction, Crane Service

Industry/Entity Type

Contact Information for Business Card

Name, Phone Number, email address

Colors

Designer to choose colors to be used in the design.

Requirements
Nice to have
• It would be great to have either a mountain or one of the attached cranes as a backdrop on the rear of the card. Simple watermarks and/or Debossing is also great

```html
<!DOCTYPE html>
<html lang="en">
<head>
<meta charset="utf-8">
<title>Ridgely Forge – Business Card</title>
<link rel="stylesheet" href="https://fonts.googleapis.com/css2?family=Open+Sans:wght@400;600;700&display=swap">
<style>
  :root {
    --page-bg: #232323;
    --card-bg: #1f1f23;
    --card-back-bg: #1c1c20;
    --teal: #25685f;
    --teal-bright: #2b7a6f;
    --white: #ffffff;
    --text-light: #f2f2f2;
    --deboss: #141417;
    --divider: #bdbdbd;
  }
  * { box-sizing: border-box; margin: 0; padding: 0; }
  html, body {
    width: 1200px; height: 780px; overflow: hidden;
    background: var(--page-bg);
    font-family: "Open Sans", Arial, sans-serif;
  }
  .canvas {
    position: relative; width: 1200px; height: 780px;
    display: flex; align-items: center; justify-content: center; gap: 40px;
  }
  .card {
    position: relative; width: 560px; height: 320px; flex: none;
    border-radius: 4px; overflow: hidden;
  }
  /* Front */
  .card--front { background: var(--card-bg); }
  .brand {
    position: absolute; left: 34px; top: 58px;
    display: flex; align-items: center; gap: 12px;
  }
  .brand__dot {
    flex: none;
    width: 44px; height: 44px; border-radius: 50%;
    background: var(--teal);
  }
  .brand__name {
    white-space: nowrap;
    font-weight: 700; font-size: 20px; letter-spacing: 0.5px;
    color: var(--teal-bright); text-transform: uppercase; line-height: 1;
  }
  .divider {
    position: absolute; left: 312px; top: 40px;
    width: 1px; height: 180px; background: var(--divider);
    transform: rotate(14deg); transform-origin: top left;
  }
  .person { position: absolute; left: 334px; top: 96px; }
  .person__name {
    white-space: nowrap;
    font-weight: 700; font-size: 30px; color: var(--teal-bright); line-height: 1.1;
  }
  .person__title {
    font-size: 14px; color: var(--text-light); margin-top: 2px;
  }
  .contacts { list-style: none; margin-top: 16px; }
  .contacts li {
    display: flex; align-items: center; gap: 8px; white-space: nowrap;
    font-size: 14px; color: var(--text-light); line-height: 1.55;
  }
  .contacts svg { width: 13px; height: 13px; flex: none; fill: var(--teal-bright); }
  .address-band {
    position: absolute; left: 0; bottom: 0; width: 100%; height: 38px;
    background: var(--teal);
    display: flex; align-items: center; padding-left: 24px;
    font-size: 14px; color: var(--white); white-space: nowrap;
  }
  .address-band__end {
    position: absolute; right: 0; top: 0; width: 74px; height: 38px;
    background: var(--white);
  }
  /* Back */
  .card--back { background: var(--card-back-bg); }
  .deboss {
    position: absolute; left: 50%; top: 50%;
    transform: translate(-50%, -50%);
    display: flex; align-items: center; gap: 16px;
  }
  .deboss__dot {
    flex: none;
    width: 74px; height: 74px; border-radius: 50%; background: var(--deboss);
  }
  .deboss__name {
    white-space: nowrap;
    font-weight: 700; font-size: 38px; letter-spacing: 1px;
    text-transform: uppercase; color: var(--deboss); line-height: 1;
  }
</style>
</head>
<body>
<main class="canvas">
  <section class="card card--front" aria-label="Card front">
    <div class="brand">
      <span class="brand__dot"></span>
      <span class="brand__name">Ridgely Forge</span>
    </div>
    <span class="divider"></span>
    <div class="person">
      <h1 class="person__name">Dalen Voss</h1>
      <p class="person__title">Managing Director</p>
      <ul class="contacts">
        <li>
          <svg viewBox="0 0 24 24" aria-hidden="true"><path d="M6.6 10.8a15 15 0 0 0 6.6 6.6l2.2-2.2a1 1 0 0 1 1-.25 11.4 11.4 0 0 0 3.6.57 1 1 0 0 1 1 1V20a1 1 0 0 1-1 1A17 17 0 0 1 3 4a1 1 0 0 1 1-1h3.5a1 1 0 0 1 1 1c0 1.250.2 2.45.57 3.57a1 1 0 0 1-.25 1z"/></svg>
          (555) 214-3096
        </li>
        <li>
          <svg viewBox="0 0 24 24" aria-hidden="true"><path d="M2 5h20v14H2zm2 2v.5l8 5 8-5V7z"/></svg>
          hello@ridgelyforge.com
        </li>
        <li>
          <svg viewBox="0 0 24 24" aria-hidden="true"><circle cx="12" cy="12" r="10"/></svg>
          www.ridgelyforge.com
        </li>
      </ul>
    </div>
    <div class="address-band">
      418 Cedar Hollow Rd. Suite 12 Larkfield, TX 75001
      <span class="address-band__end"></span>
    </div>
  </section>

  <section class="card card--back" aria-label="Card back">
    <div class="deboss">
      <span class="deboss__dot"></span>
      <span class="deboss__name">Ridgely Forge</span>
    </div>
  </section>
</main>
</body>
</html>
```